Classy business card for accounting firm

We're looking for a new business card for our accounting firm. Our logo was designed by Brandolith, so all of the design info we would like to use has been provided. The specific font provided isn't required to be used.

We want the card to look classy and elegent. Probably more minimalistic, but still with some pops of color.

The options we would like to include on the card are as follows:
1. Main office phone line
2. Direct phone line
3. Email address
4. Website URL
5. Name
6. Title (CEO, President, etc.)
7. Firm Address

The design and card should be double sided!!! The drop down box in the project brief for some reason is defaulting to single sided. Not sure why this is happening.

Thanks!

Contact Information for Business Card

The options we would like to include on the card are as follows: 1. Main office phone line 2. Direct phone line 3. Email address 4. Website URL 5. Name 6. Title (CEO, President, etc.) 7. Firm Address

Requirements
Must have
• Card must be double sided.

```html
<!DOCTYPE html>
<html lang="en">
<head>
<meta charset="utf-8">
<title>Fairledger Associates — Business Card</title>
<link href="https://fonts.googleapis.com/css2?family=Montserrat:wght@500;600&family=Lato:wght@400&display=swap" rel="stylesheet">
<style>
  :root {
    --backdrop: #2b2b2b;
    --card: #ffffff;
    --ink: #5a5a5a;
    --ink-soft: #6b6b6b;
    --orange: #f47a1f;
  }
  * { box-sizing: border-box; margin: 0; padding: 0; }
  html, body { width: 1165px; height: 1200px; overflow: hidden; }
  body {
    background: var(--backdrop);
    display: flex;
    flex-direction: column;
    align-items: center;
    justify-content: center;
    gap: 64px;
    font-family: "Lato", sans-serif;
  }
  .card {
    position: relative;
    width: 780px;
    height: 446px;
    background: var(--card);
    border-radius: 34px;
    overflow: hidden;
  }
  .brand {
    display: flex;
    align-items: center;
    gap: 14px;
  }
  .brand-mark {
    width: 26px;
    height: 26px;
    background: var(--orange);
    flex: none;
  }
  .brand-name {
    font-family: "Montserrat", sans-serif;
    font-weight: 500;
    color: var(--ink);
    letter-spacing: 0.06em;
    white-space: nowrap;
  }

  /* Front */
  .card-front { display: flex; align-items: center; justify-content: center; }
  .card-front .brand-name { font-size: 34px; }

  /* Back */
  .card-back .brand { position: absolute; left: 58px; top: 100px; }
  .card-back .brand-name { font-size: 30px; }
  .person { position: absolute; left: 58px; top: 192px; }
  .person-name {
    font-family: "Montserrat", sans-serif;
    font-weight: 600;
    font-size: 24px;
    color: var(--orange);
    letter-spacing: 0.03em;
  }
  .person-title { font-size: 16px; color: var(--ink-soft); margin-top: 2px; }
  .address { margin-top: 22px; font-size: 15px; color: var(--ink-soft); line-height: 1.35; }
  .contacts { list-style: none; margin-top: 18px; font-size: 15px; color: var(--ink-soft); line-height: 1.45; }
  .contacts li { display: flex; align-items: center; gap: 10px; }
  .contacts svg { width: 12px; height: 12px; fill: none; stroke: var(--orange); stroke-width: 2; flex: none; }
</style>
</head>
<body>
  <section class="card card-front">
    <div class="brand">
      <span class="brand-mark"></span>
      <span class="brand-name">FAIRLEDGER ASSOCIATES</span>
    </div>
  </section>

  <section class="card card-back">
    <div class="brand">
      <span class="brand-mark"></span>
      <span class="brand-name">FAIRLEDGER ASSOCIATES</span>
    </div>
    <div class="person">
      <p class="person-name">DANIEL HART</p>
      <p class="person-title">President</p>
      <p class="address">1129 32th Street Here<br>400 Address Here, DC 20036</p>
      <ul class="contacts">
        <li><svg viewBox="0 0 12 12"><path d="M2 1.5l2 0 1 2.5-1.3 1a6 6 0 0 0 3.3 3.3l1-1.3 2.5 1v2c-5 0-8.5-3.5-8.5-8.5z"/></svg>000 0000 000</li>
        <li><svg viewBox="0 0 12 12"><rect x="3" y="1" width="6" height="10" rx="1"/></svg>000 0000 000</li>
        <li><svg viewBox="0 0 12 12"><rect x="1" y="2.5" width="10" height="7"/><path d="M1 2.5l5 4 5-4"/></svg>info@emailhere.com</li>
        <li><svg viewBox="0 0 12 12"><circle cx="6" cy="6" r="5"/><path d="M1 6h10M6 1c2 2.5 2 7.5 0 10M6 1c-2 2.5-2 7.5 0 10"/></svg>www.websitehere.com</li>
      </ul>
    </div>
  </section>
</body>
</html>
```